Fitness business need 3x3 card to promote 6wk boot camp nutrition challenge

Hi, we're looking for someone to make our current card look better and more modern. We want to keep the text the same, but we want a better design. We also want to keep the woman on the front of the card. The card is for both men and women so we want it to feel inclusive and bright. The idea is to make the card look more modern. We want some pops of color. The main feature is to promote the pricing on the back of the card. It would be nice if that continues to look like a coupon or if it stands out with a bright color or background.

Target Market(s)

Men and women looking to get in shape

Industry/Entity Type

Fitness

Font styles to use
Serif
Sans Serif

Colors
3176b5
0255a3
33a6d7
f37122
ec1f27

Requirements
Must have
• front and back, use pic of women provided

```html
<!DOCTYPE html>
<html lang="en">
<head>
<meta charset="utf-8">
<title>6WK Fitness &amp; Nutrition Boot Camp – Cards</title>
<link href="https://fonts.googleapis.com/css2?family=Oswald:wght@300;400;500;600&display=swap" rel="stylesheet">
<style>
  :root {
    --orange: #f37122;
    --blue: #3a9fd0;
    --blue-deep: #2f8cbd;
    --band-grey: #e4e4e4;
    --stripe-white: #f7f7f7;
    --ink-dark: #2e3841;
    --white: #ffffff;
    --backdrop: #ebe6e0;
    --photo-light: #b9b9b9;
    --photo-dark: #3b3b3b;
  }
  * { margin: 0; padding: 0; box-sizing: border-box; }
  html, body {
    width: 1200px; height: 663px; overflow: hidden;
    background: var(--backdrop);
    font-family: "Oswald", "Arial Narrow", sans-serif;
  }
  .stage { position: relative; width: 1200px; height: 663px; }
  .card {
    position: absolute; top: 89px; width: 485px; height: 485px;
    overflow: hidden; box-shadow: 0 6px 18px rgba(0,0,0,.25);
  }
  .card--front { left: 87px; }
  .card--back { left: 628px; }
  .card__art { position: absolute; inset: 0; }
  .card__text { position: absolute; color: var(--white); white-space: nowrap; }

  /* front */
  .front__brand { right: 18px; top: 20px; font-size: 31px; font-weight: 500; letter-spacing: .5px; }
  .front__title {
    left: 23px; top: 72px; font-size: 35px; line-height: 40px; font-weight: 500;
    text-shadow: 2px 2px 3px rgba(0,0,0,.35);
  }
  .accent-orange { color: var(--orange); }
  .accent-dark { color: var(--ink-dark); }
  .front__dates { left: 67px; top: 252px; font-size: 22px; line-height: 30px; font-weight: 300; }
  .front__cta { left: 27px; top: 367px; font-size: 25px; font-weight: 500; }
  .front__url { left: 29px; top: 414px; font-size: 16px; font-weight: 500; letter-spacing: .5px; }

  /* back */
  .back__headline {
    left: 0; width: 485px; top: 72px; text-align: center;
    font-size: 32px; font-weight: 500; text-shadow: 1px 1px 2px rgba(0,0,0,.25);
  }
  .back__perks {
    left: 0; width: 485px; top: 140px; text-align: center;
    font-size: 17.5px; line-height: 31px; font-weight: 300;
  }
  .back__price { left: 45px; width: 140px; top: 288px; text-align: center; font-size: 48px; font-weight: 500; line-height: 1; }
  .back__duration { left: 45px; width: 140px; top: 342px; text-align: center; font-size: 17px; font-weight: 500; color: var(--orange); }
  .back__title {
    right: 28px; top: 264px; text-align: right;
    font-size: 38px; line-height: 43px; font-weight: 500;
    text-shadow: 2px 2px 3px rgba(0,0,0,.3);
  }
  .back__title .accent-dark { text-shadow: 1px 1px 0 rgba(255,255,255,.25); }
  .back__cta { left: 20px; top: 421px; font-size: 20px; font-weight: 500; }
  .back__url { left: 20px; top: 458px; font-size: 13.5px; font-weight: 500; color: var(--ink-dark); letter-spacing: .4px; }
  .back__brand { right: 20px; top: 416px; font-size: 29px; font-weight: 500; }
</style>
</head>
<body>
<main class="stage">

  <section class="card card--front" aria-label="Front of card">
    <svg class="card__art" width="485" height="485" viewBox="0 0 485 485">
      <rect width="485" height="485" fill="var(--band-grey)"/>
      <polygon points="0,0 88,0 128,49 0,49" fill="var(--orange)"/>
      <polygon points="100,0 120,0 160,49 140,49" fill="var(--stripe-white)"/>
      <polygon points="132,0 152,0 192,49 172,49" fill="var(--orange)"/>
      <rect y="49" width="485" height="401" fill="var(--blue)"/>
      <defs>
        <linearGradient id="photoTone" x1="0" y1="0" x2="1" y2="1">
          <stop offset="0" stop-color="var(--photo-light)"/>
          <stop offset="1" stop-color="var(--photo-dark)"/>
        </linearGradient>
      </defs>
      <polygon points="179,49 485,49 485,450 386,450" fill="url(#photoTone)"
               role="img" aria-label="Black and white photo of a woman in athletic wear sitting beside a medicine ball"/>
      <polygon points="265,10 485,10 485,79 299,79" fill="var(--orange)"/>
      <polyline points="25,258 37,273 25,288" fill="none" stroke="var(--white)" stroke-width="5"/>
      <polyline points="39,258 51,273 39,288" fill="none" stroke="var(--white)" stroke-width="5"/>
      <polygon points="0,364 258,364 248,404 0,404" fill="var(--orange)"/>
      <polygon points="300,450 318,450 340,485 322,485" fill="var(--orange)"/>
      <polygon points="330,450 348,450 370,485 352,485" fill="var(--orange)"/>
      <polygon points="360,450 378,450 400,485 382,485" fill="var(--stripe-white)"/>
    </svg>
    <div class="card__text front__brand">BRANDNAME</div>
    <h1 class="card__text front__title"><span class="accent-orange">6WK</span> FITNESS<br>&amp; NUTRITION<br><span class="accent-orange">BOOT CAMP</span></h1>
    <p class="card__text front__dates">October 2nd<br>to November 11th</p>
    <p class="card__text front__cta">SIGN UP TODAY!</p>
    <p class="card__text front__url">www.fitcampsix.com</p>
  </section>

  <section class="card card--back" aria-label="Back of card">
    <svg class="card__art" width="485" height="485" viewBox="0 0 485 485">
      <rect width="485" height="485" fill="var(--band-grey)"/>
      <polygon points="0,26 66,26 84,49 0,49" fill="var(--orange)"/>
      <polygon points="80,26 98,26 116,49 98,49" fill="var(--orange)"/>
      <polygon points="112,26 130,26 148,49 130,49" fill="var(--orange)"/>
      <rect y="49" width="485" height="397" fill="var(--blue)"/>
      <rect y="134" width="485" height="106" fill="var(--orange)"/>
      <defs>
        <radialGradient id="badgeTone" cx=".4" cy=".35" r=".7">
          <stop offset="0" stop-color="#4a4a4a"/>
          <stop offset="1" stop-color="#151515"/>
        </radialGradient>
      </defs>
      <g class="price-badge">
        <circle cx="115" cy="330" r="69" fill="none" stroke="#1c1c1c" stroke-width="10" stroke-dasharray="7 5.5"/>
        <circle cx="115" cy="330" r="67" fill="url(#badgeTone)"/>
      </g>
      <polygon points="0,420 185,420 178,452 0,452" fill="var(--orange)"/>
      <polygon points="300,413 485,413 485,462 270,462" fill="var(--orange)"/>
    </svg>
    <h2 class="card__text back__headline"><span class="accent-dark">NO</span> BARBELLS! <span class="accent-dark">NO</span> HEAVY WEIGHTS!</h2>
    <p class="card__text back__perks">Burn fat, build muscle &amp; have fun!<br>Tons of classes led by world-class coaches.<br>Personalized nutrition planning, prizes, and more!</p>
    <p class="card__text back__price">$249</p>
    <p class="card__text back__duration">6WEEKS</p>
    <h1 class="card__text back__title"><span class="accent-dark">6WK</span> FITNESS<br>&amp; NUTRITION<br><span class="accent-dark">BOOT CAMP</span></h1>
    <p class="card__text back__cta">SIGN UP TODAY!</p>
    <p class="card__text back__url">www.fitcampsix.com</p>
    <div class="card__text back__brand">BRANDNAME</div>
  </section>

</main>
</body>
</html>
```